Holiday Greeting Card

Harbor Beamworks is sending out a non-religious New Years greeting card to those businesses and individuals who donate materials to our retail outlet. Included in the card is a reminder to donate. Harbor Beamworks is a nonprofit building materials reuse center. We accept donations of salvaged and surplus building materials and make them available to the community for free or at very low cost. Our mission is to lift up local communities by reducing waste, creating green jobs and making affordable building materials available to the local community. Our website is harborbeamworks.org
Updates

Hi there!!

We've boiled it down to two options but won't be able to make a final decision until our boss comes in to the office next week and we get a group consensus. We won't be seeking any more submissions, but will be in touch with those of you who we'd like to stay in touch with!

Thanks again for all of your incredible work!
Tess

Target Market(s)

Our donors, who are mostly small businesses in the construction trade industry

Requirements
Must have
• Our Harbor Beamworks logo and the attached text. There is flexibility in formatting.
Nice to have
• Festive feeling that merges a "Happy New Year" message with construction materials
Should not have
• Anything Religious

```html
<!DOCTYPE html>
<html lang="en">
<head>
<meta charset="utf-8">
<title>Harbor Beamworks – New Year Greeting Card</title>
<link href="https://fonts.googleapis.com/css2?family=Boogaloo&family=Cabin:wght@600;700&display=swap" rel="stylesheet">
<style>
  :root {
    --page-grey: #f1f1f1;
    --sheet: #ffffff;
    --frame-green: #44f513;
    --trim-green: #5ee83a;
    --lime: #d8fb1f;
    --title-green: #2fb52f;
    --deep-green: #1f7d1f;
    --sky-blue: #3d8ee6;
    --pale-blue: #9fd3ff;
    --cyan: #00f6ff;
    --logo-navy: #2a1a7a;
    --wood: #c9a779;
    --brick: #d8463a;
    --mesh: #b9bec3;
    --rebar: #6f767c;
  }
  html, body {
    margin: 0;
    width: 1200px;
    height: 819px;
    overflow: hidden;
    background: var(--page-grey);
  }
  .card-spread { display: block; width: 1200px; height: 819px; }
  .headline { font-family: "Boogaloo", cursive; }
  .body-copy { font-family: "Cabin", sans-serif; font-weight: 700; }
  .brand-name { font-family: "Cabin", sans-serif; font-weight: 700; fill: var(--logo-navy); }
</style>
</head>
<body>
<svg class="card-spread" viewBox="0 0 1265 862" preserveAspectRatio="none" xmlns="http://www.w3.org/2000/svg">
  <!-- sheet -->
  <rect class="sheet" x="31" y="31" width="1204" height="802" fill="var(--sheet)"/>
  <rect class="trim" x="131" y="108" width="1003" height="640" fill="none" stroke="var(--trim-green)" stroke-width="2"/>
  <line class="fold" x1="632" y1="108" x2="632" y2="748" stroke="var(--trim-green)" stroke-width="2"/>

  <!-- inside-left panel: materials -->
  <g class="panel-left">
    <rect x="158" y="141" width="448" height="575" fill="var(--sheet)"/>
    <rect role="img" aria-label="Photo of stacked reclaimed lumber" x="186" y="159" width="171" height="111" fill="var(--wood)"/>
    <rect role="img" aria-label="Photo of stacked red and pink bricks" x="399" y="159" width="169" height="111" fill="var(--brick)"/>
    <rect role="img" aria-label="Photo of steel pipes and wire mesh panels" x="228" y="284" width="225" height="134" fill="var(--mesh)"/>
    <rect role="img" aria-label="Photo of bundled steel rebar" x="399" y="436" width="187" height="112" fill="var(--rebar)"/>
    <path class="swoop" d="M160,408 C175,420 200,430 260,435 C320,440 340,460 360,510 C380,560 400,610 450,625 C480,635 510,630 520,640 C530,655 540,690 548,716" fill="none" stroke="var(--frame-green)" stroke-width="6"/>
    <g class="brand">
      <circle cx="214" cy="664" r="18" fill="var(--logo-navy)"/>
      <text class="brand-name" x="240" y="672" font-size="19">HARBOR BEAMWORKS</text>
    </g>
    <rect x="158" y="141" width="448" height="575" fill="none" stroke="var(--frame-green)" stroke-width="7"/>
  </g>

  <!-- inside-right panel: greeting -->
  <g class="panel-right">
    <rect x="659" y="141" width="447" height="575" fill="var(--lime)"/>
    <polygon class="burst" fill="var(--sheet)" points="880,150 860,205 700,185 830,235 670,300 840,265 800,330 880,270 960,300 930,255 1100,285 950,225 1100,160 920,205 905,145"/>
    <path class="lower-field" d="M1106,405 C1090,415 1000,420 940,440 C900,460 880,520 860,560 C830,610 790,630 750,635 C730,640 725,680 722,716 L1106,716 Z" fill="var(--sheet)"/>
    <path d="M1106,405 C1090,415 1000,420 940,440 C900,460 880,520 860,560 C830,610 790,630 750,635 C730,640 725,680 722,716" fill="none" stroke="var(--frame-green)" stroke-width="6"/>
    <polygon class="sparkle" fill="var(--cyan)" points="985,410 992,465 1065,462 998,490 1020,560 980,505 905,530 960,485 915,440 972,462"/>

    <text class="headline" x="880" y="214" text-anchor="middle" font-size="40" fill="var(--title-green)" stroke="var(--sheet)" stroke-width="1">HAPPY NEW YEAR</text>
    <text class="headline" x="1000" y="265" text-anchor="middle" font-size="30" fill="var(--sheet)" stroke="var(--pale-blue)" stroke-width="1.5" transform="rotate(18 1000 255)">2014</text>
    <text class="headline" x="898" y="266" text-anchor="middle" font-size="22" fill="var(--trim-green)" stroke="var(--sheet)" stroke-width="0.6">From</text>
    <text class="headline" x="826" y="296" text-anchor="middle" font-size="24" fill="var(--trim-green)" stroke="var(--sheet)" stroke-width="0.6">Harbor Beamworks !</text>

    <text class="body-copy" font-size="24" fill="var(--deep-green)">
      <tspan x="671" y="437">Thank you for</tspan>
      <tspan x="671" y="468">helping us lift up</tspan>
      <tspan x="671" y="499">Communities in</tspan>
    </text>
    <text class="body-copy" x="670" y="541" font-size="33" fill="var(--sky-blue)">2013</text>
    <text class="body-copy" font-size="16" fill="var(--sky-blue)">
      <tspan x="889" y="568">We look forward to</tspan>
      <tspan x="889" y="589">working with you again</tspan>
      <tspan x="889" y="610">in the new year !</tspan>
    </text>

    <g class="brand">
      <circle cx="870" cy="664" r="18" fill="var(--logo-navy)"/>
      <text class="brand-name" x="895" y="672" font-size="19">HARBOR BEAMWORKS</text>
    </g>
    <rect x="659" y="141" width="447" height="575" fill="none" stroke="var(--frame-green)" stroke-width="7"/>
  </g>
</svg>
</body>
</html>
```